Brightwell Support! Virtual Assistant business needs a Website

I have started an online business called "Brightwell Support". I offer all the same types of services as a typical Personal Assistant, only remotely. For example, document formatting and editing (word, powerpoint, excel etc.), email and calendar management, appointments and bookings, document creation, reports, travel and event management and so on.

I already have a logo ready to go, however I have yet to finalise the copy for the site, so if you could create the pages with pictures, and I can fill in the wording at a later date.

Target Market(s)

Anyone who is overloaded at work and needs someone to take the admin work off their hands.

Number of Pages Required

4 page

Font styles to use
Sans Serif
Script
Other font styles liked:
• Gotham Medium is used in my font

Colors

Designer to choose colors to be used in the design.

Requirements
Must have
• Home Page
• About Page
• Pricing Page
• Contact Page
Nice to have
• Pictures and a professional design, I like white space and simple design.
Should not have
• cartoons or anything unprofessional looking.

```html
<!DOCTYPE html>
<html lang="en">
<head>
<meta charset="utf-8">
<title>Brightwell Support</title>
<link href="https://fonts.googleapis.com/css2?family=Montserrat:wght@400;500;600;700&family=Lato:wght@400;700&display=swap" rel="stylesheet">
<style>
:root{
  --blue:#16479b;
  --blue-dark:#123c86;
  --ink:#2b2b2b;
  --muted:#555;
  --line:#dcdcdc;
  --grey-bg:#efefef;
  --price-grey:#cfcfcf;
  --white:#fff;
}
*{box-sizing:border-box;margin:0;padding:0}
html,body{width:1200px;height:3930px;overflow:hidden}
body{position:relative;font-family:'Lato',sans-serif;color:var(--ink);background:var(--white)}
.abs{position:absolute}
h2.section-title{position:absolute;left:0;width:1200px;text-align:center;font-family:'Montserrat',sans-serif;font-size:42px;font-weight:500;color:var(--blue)}
h2.section-title b{font-weight:700}
h2.section-title span{color:#5a6f96;font-weight:400}
.on-blue{color:var(--white)!important}

/* header + hero */
.hero{left:0;top:0;width:1200px;height:702px;background:linear-gradient(100deg,#d8dde3 0%,#eceff2 40%,#cfd3d8 70%,#b9bec4 100%)}
.header{left:0;top:0;width:1200px;height:110px;background:rgba(255,255,255,.82)}
.brand{left:78px;top:26px;display:flex;align-items:center;gap:14px;font-family:'Montserrat',sans-serif;font-weight:700;font-size:34px;color:var(--blue)}
.brand i{width:54px;height:54px;border-radius:50%;background:var(--blue);display:block}
.nav{right:80px;top:44px;display:flex;gap:54px;font-family:'Montserrat',sans-serif;font-weight:600;font-size:16px;color:var(--ink)}
.nav .active{color:var(--blue)}
.hero-title{left:80px;top:312px;font-family:'Montserrat',sans-serif;font-weight:600;font-size:38px;line-height:52px;color:var(--blue)}
.btn-solid{background:var(--blue);color:var(--white);font-family:'Montserrat',sans-serif;font-weight:700;font-size:18px;display:flex;align-items:center;justify-content:center;border-radius:3px}
.hero-btn{left:78px;top:440px;width:196px;height:52px}
.dots{left:556px;top:648px;display:flex;gap:12px}
.dots i{width:20px;height:20px;border-radius:50%;background:#8f97a3;display:block}
.dots i:first-child{background:var(--blue)}

/* about */
.about-title{left:82px;top:752px;font-family:'Montserrat',sans-serif;font-size:42px;font-weight:700;color:var(--blue)}
.about-title span{font-weight:400;color:#4a5a7a}
.about-text{left:82px;top:828px;width:520px;font-size:15px;line-height:25px;color:var(--muted)}
.about-btn{left:78px;top:1008px;width:158px;height:50px;font-size:16px}
.about-photo{left:706px;top:764px;width:416px;height:298px;border:5px solid var(--blue);padding:10px}
.about-photo div{width:100%;height:100%;background:linear-gradient(90deg,#7e8894,#dfe4ea 50%,#9aa4b0)}

/* pricing */
.pricing{left:0;top:1127px;width:1200px;height:539px;background:var(--blue)}
.plan{top:1263px;width:272px;height:340px;background:var(--white);border-radius:6px;text-align:center}
.plan h3{font-family:'Montserrat',sans-serif;font-weight:500;font-size:25px;color:#333;height:66px;line-height:66px;border-bottom:2px solid var(--line)}
.plan.featured h3{color:var(--blue);border-bottom-color:var(--blue)}
.price{margin:20px auto 0;width:157px;height:50px;line-height:50px;background:var(--price-grey);font-size:24px;color:#444;border-radius:2px}
.plan.featured .price{background:var(--blue);color:var(--white)}
.plan p{font-size:15px;color:var(--muted);line-height:34px;margin-top:16px}
.plan p + p{margin-top:0}
.buy{margin:20px auto 0;width:139px;height:42px;line-height:40px;border:1px solid var(--line);font-family:'Montserrat',sans-serif;font-weight:500;font-size:15px;color:#333;border-radius:3px}
.plan.featured .buy{background:var(--blue);border-color:var(--blue);color:var(--white);font-weight:600}

/* services */
.service{width:313px;height:228px;border:2px solid #e2e2e2;border-radius:3px;text-align:center;padding-top:26px}
.service svg{width:52px;height:52px}
.service h4{font-family:'Lato',sans-serif;font-weight:400;font-size:18px;color:var(--blue);margin-top:12px}
.service p{font-size:14px;line-height:22px;color:var(--muted);margin:6px auto 0;width:240px}
.service a{display:inline-block;margin-top:4px;font-size:14px;font-weight:700;color:var(--blue);text-decoration:underline}

/* newsletter */
.newsletter{left:0;top:2363px;width:1200px;height:317px;background:var(--blue)}
.news-text{left:310px;top:2493px;width:580px;text-align:center;color:var(--white);font-size:15px;line-height:27px}
.field{height:53px;background:var(--white);border-radius:3px;font-size:14px;color:#666;padding:0 16px;display:flex;align-items:center}
.subscribe{left:854px;top:2567px;width:157px;height:53px;border:2px solid var(--white);border-radius:3px;color:var(--white);font-family:'Montserrat',sans-serif;font-weight:700;font-size:17px;display:flex;align-items:center;justify-content:center}

/* contact */
.input{border:1px solid #d6d6d6;border-radius:3px;box-shadow:0 1px 3px rgba(0,0,0,.12);font-size:14px;color:#555;padding:16px 12px;background:var(--white)}
.submit{left:84px;top:3052px;width:655px;height:53px;font-size:17px}
.info{left:799px;display:flex;gap:20px;font-size:15px;line-height:24px;color:var(--muted);width:300px}
.info svg{flex:none;width:20px;height:20px;fill:var(--blue);margin-top:2px}

/* latest news */
.latest{left:0;top:3160px;width:1200px;height:560px;background:var(--grey-bg)}
.post{top:3296px;width:322px}
.post .thumb{position:relative;height:210px;background:linear-gradient(135deg,#8a95a3,#d7dce2)}
.post .date{position:absolute;left:0;top:0;width:50px;height:58px;background:var(--blue);color:var(--white);text-align:center;font-size:28px;line-height:34px;padding-top:2px}
.post .date small{display:block;font-size:12px;line-height:16px}
.post h5{font-family:'Lato',sans-serif;font-weight:400;font-size:18px;color:var(--blue);margin-top:20px}
.post p{font-size:14px;line-height:25px;color:var(--muted);margin-top:6px}
.post a{display:block;margin-top:6px;font-size:14px;font-weight:700;color:var(--blue);text-decoration:underline}

/* footer */
.footer{left:0;top:3720px;width:1200px;height:210px;background:var(--blue)}
.foot-nav{left:0;top:3762px;width:1200px;display:flex;justify-content:center;gap:44px;color:var(--white);font-size:15px}
.social{left:0;top:3783px;width:1200px;display:flex;justify-content:center;gap:14px}
.social i{width:42px;height:42px;border-radius:50%;border:2px solid var(--white);display:block}
.social i:first-child{background:var(--white)}
.foot-line{left:78px;top:3866px;width:1044px;height:1px;background:rgba(255,255,255,.45)}
.copy{left:0;top:3888px;width:1200px;text-align:center;color:var(--white);font-size:14px}
</style>
</head>
<body>

<!-- Hero -->
<div class="abs hero" role="img" aria-label="Photo of a professional woman working on a laptop in a bright office"></div>
<header class="abs header"></header>
<div class="abs brand"><i></i>Brightwell Support</div>
<nav class="abs nav"><span class="active">HOME</span><span>ABOUT US</span><span>PRICING</span><span>CONTACT US</span></nav>
<h1 class="abs hero-title">LOREM IPSUM IS SIMPLY<br>DUMMY</h1>
<div class="abs btn-solid hero-btn">CONTACT US NOW!</div>
<div class="abs dots"><i></i><i></i><i></i></div>

<!-- About -->
<h2 class="abs about-title">About <span>Us</span></h2>
<p class="abs about-text">Lorem Ipsum is simply dummy text of the printing and typesetting industry. Lorem Ipsum has been the industry's standard dummy text ever since the 1500s, when an unknown printer took a galley of type and scrambled it to make a type specimen book. It has survived not only five centuries, but also the leap into electronic typesetting, remaining essentially unchanged.</p>
<div class="abs btn-solid about-btn">LEARN MORE</div>
<div class="abs about-photo"><div role="img" aria-label="Photo of two business people shaking hands in an office"></div></div>

<!-- Pricing -->
<section class="abs pricing"></section>
<h2 class="section-title on-blue" style="top:1180px">Our Pricing</h2>
<div class="abs plan" style="left:173px"><h3>BASIC</h3><div class="price">$ 200.00</div><p>Lorem Ipsum is simply</p><p>Lorem Ipsum is</p><p>Lorem Ipsum simply</p><div class="buy">BUY NOW</div></div>
<div class="abs plan featured" style="left:464px"><h3>STANDARD</h3><div class="price">$ 200.00</div><p>Lorem Ipsum is simply</p><p>Lorem Ipsum is</p><p>Lorem Ipsum simply</p><div class="buy">BUY NOW</div></div>
<div class="abs plan" style="left:755px"><h3>ULTIMATED</h3><div class="price">$ 200.00</div><p>Lorem Ipsum is simply</p><p>Lorem Ipsum is</p><p>Lorem Ipsum simply</p><div class="buy">BUY NOW</div></div>

<!-- Services -->
<h2 class="section-title" style="top:1722px"><b>Our</b> <span>Services</span></h2>
<div class="abs service" style="left:84px;top:1797px">
  <svg viewBox="0 0 52 52" fill="none" stroke="#16479b" stroke-width="2.5"><path d="M12 4h20l10 10v34H12z"/><path d="M32 4v10h10"/><path d="M27 38V24m-6 6 6-6 6 6"/></svg>
  <h4>Document formatting and editing</h4><p>Lorem Ipsum is simply dummy text of the printing and typesetting</p><a>Read more...</a></div>
<div class="abs service" style="left:443px;top:1797px">
  <svg viewBox="0 0 52 52" fill="none" stroke="#16479b" stroke-width="2.5"><rect x="5" y="9" width="34" height="30" rx="2"/><path d="M5 17h34M12 5v8M32 5v8"/><circle cx="38" cy="38" r="10" fill="#fff"/><path d="M38 32v6l4 3"/></svg>
  <h4>E-mail and calendar management</h4><p>Lorem Ipsum is simply dummy text of the printing and typesetting</p><a>Read more...</a></div>
<div class="abs service" style="left:802px;top:1797px">
  <svg viewBox="0 0 52 52" fill="#16479b"><rect x="12" y="20" width="28" height="22" rx="3"/><path d="M19 20v-5a7 7 0 0 1 14 0v5" fill="none" stroke="#16479b" stroke-width="3"/><circle cx="26" cy="30" r="3" fill="#fff"/></svg>
  <h4>Appointments and bookings</h4><p>Lorem Ipsum is simply dummy text of the printing and typesetting</p><a>Read more...</a></div>
<div class="abs service" style="left:84px;top:2070px">
  <svg viewBox="0 0 52 52" fill="none" stroke="#16479b" stroke-width="2.5"><rect x="12" y="4" width="28" height="44" rx="3"/><circle cx="26" cy="17" r="5"/><path d="M18 30h16M18 36h16M18 42h10"/></svg>
  <h4>Document creation</h4><p>Lorem Ipsum is simply dummy text of the printing and typesetting</p><a>Read more...</a></div>
<div class="abs service" style="left:443px;top:2070px">
  <svg viewBox="0 0 52 52" fill="none" stroke="#16479b" stroke-width="2.5"><rect x="9" y="6" width="34" height="42" rx="2"/><path d="M19 6V3h14v3"/><path d="M15 18l2 2 4-4M15 29l2 2 4-4M15 40l2 2 4-4M26 18h11M26 29h11M26 40h11"/></svg>
  <h4>Reports</h4><p>Lorem Ipsum is simply dummy text of the printing and typesetting</p><a>Read more...</a></div>
<div class="abs service" style="left:802px;top:2070px">
  <svg viewBox="0 0 52 52" fill="none" stroke="#16479b" stroke-width="2.5"><rect x="5" y="9" width="40" height="36" rx="2"/><path d="M5 18h40M14 4v9M36 4v9"/><path d="M12 25h5v5h-5zM23 25h5v5h-5zM34 25h5v5h-5zM12 35h5v5h-5zM23 35h5v5h-5z"/></svg>
  <h4>Travel and event management</h4><p>Lorem Ipsum is simply dummy text of the printing and typesetting</p><a>Read more...</a></div>

<!-- Newsletter -->
<section class="abs newsletter"></section>
<h2 class="section-title on-blue" style="top:2416px">Newsletter</h2>
<p class="abs news-text">Lorem Ipsum is simply dummy text of the printing and typesetting industry. Lorem Ipsum has been the industry's</p>
<div class="abs field" style="left:189px;top:2567px;width:322px">Enter Name*</div>
<div class="abs field" style="left:521px;top:2567px;width:323px">Enter E-mail*</div>
<div class="abs subscribe">SUBSCRIBE</div>

<!-- Contact -->
<h2 class="section-title" style="top:2736px"><b>Get</b> <span>In Touch</span></h2>
<div class="abs input" style="left:84px;top:2811px;width:322px;height:53px">Name</div>
<div class="abs input" style="left:415px;top:2811px;width:324px;height:53px">E-mail</div>
<div class="abs input" style="left:84px;top:2874px;width:322px;height:53px">Phone</div>
<div class="abs input" style="left:415px;top:2874px;width:324px;height:53px">Subject</div>
<div class="abs input" style="left:84px;top:2937px;width:655px;height:105px">Message</div>
<div class="abs btn-solid submit">SUBMIT</div>
<div class="abs info" style="top:2880px"><svg viewBox="0 0 24 24"><path d="M12 2a7 7 0 0 0-7 7c0 5 7 13 7 13s7-8 7-13a7 7 0 0 0-7-7zm0 9.5A2.5 2.5 0 1 1 12 6.5a2.5 2.5 0 0 1 0 5z"/></svg><span>Lorem Ipsum is simply dummy text of the printing</span></div>
<div class="abs info" style="top:2942px"><svg viewBox="0 0 24 24"><path d="M6.6 10.8a15 15 0 0 0 6.6 6.6l2.2-2.2c.3-.3.7-.4 1-.2 1.1.4 2.3.6 3.6.6.6 0 1 .4 1 1V20c0 .6-.4 1-1 1A17 17 0 0 1 3 4c0-.6.4-1 1-1h3.5c.6 0 1 .4 1 1 0 1.3.2 2.5.6 3.6.1.3 0 .7-.2 1z"/></svg><span>123 456 7890</span></div>
<div class="abs info" style="top:2984px"><svg viewBox="0 0 24 24"><path d="M3 5h18v14H3zm2 2v.5l7 5 7-5V7z" fill-rule="evenodd"/></svg><span>info@brightwellsupport.com</span></div>

<!-- Latest news -->
<section class="abs latest"></section>
<h2 class="section-title" style="top:3221px"><b>Latest</b> <span>News</span></h2>
<article class="abs post" style="left:79px"><div class="thumb" role="img" aria-label="Photo of hands working on a laptop with papers"><div class="date">24<small>Apr</small></div></div><h5>Lorem Ipsum is simply dummy text</h5><p>Lorem Ipsum is simply dummy text of the printing and typesetting industry. Lorem Ipsum has been the</p><a>Read more... »</a></article>
<article class="abs post" style="left:440px"><div class="thumb" role="img" aria-label="Photo of a laptop and phone showing a website"><div class="date">24<small>Apr</small></div></div><h5>Lorem Ipsum is simply dummy text</h5><p>Lorem Ipsum is simply dummy text of the printing and typesetting industry. Lorem Ipsum has been the</p><a>Read more... »</a></article>
<article class="abs post" style="left:802px"><div class="thumb" role="img" aria-label="Photo of three colleagues looking at a laptop together"><div class="date">24<small>Apr</small></div></div><h5>Lorem Ipsum is simply dummy text</h5><p>Lorem Ipsum is simply dummy text of the printing and typesetting industry. Lorem Ipsum has been the</p><a>Read more... »</a></article>

<!-- Footer -->
<footer class="abs footer"></footer>
<nav class="abs foot-nav"><span>Home</span><span>About Us</span><span>Pricing</span><span>Contact Us</span></nav>
<div class="abs social"><i></i><i></i><i></i><i></i></div>
<div class="abs foot-line"></div>
<p class="abs copy">©BRIGHTWELL SUPPORT - 2018. All Rights Reserved.</p>

</body>
</html>
```